Marrowgate Auctions Business Cards Design Needed

I need a business card design that is modern looking - double sided (maybe just my logo on the back, but open to suggestions) - the overall design is up to you. I want it to be easy to read - not over the top flashy. I already have a company logo which I uploaded so that needs to be used. The colors of my logo are the colors I want on the card... so blue and gray (do need to match the logo colors).

Requirements
Must have
• Would like the card to be sleek, modern and easy to ready

```html
<!DOCTYPE html>
<html lang="en">
<head>
<meta charset="utf-8">
<title>Marrowgate Auctions – Business Cards</title>
<link rel="stylesheet" href="https://fonts.googleapis.com/css2?family=Exo+2:wght@600;700&family=Roboto:wght@400;500&display=swap">
<style>
  :root {
    --brand-blue: #2a78b8;
    --brand-gray: #515151;
    --text-gray: #4a4a4a;
    --rule-gray: #c9c9c9;
    --card-white: #ffffff;
    --backdrop: #e9ebee;
  }
  * { box-sizing: border-box; margin: 0; padding: 0; }
  html, body { width: 1125px; height: 1200px; overflow: hidden; }
  body {
    background: var(--backdrop);
    position: relative;
    font-family: "Roboto", Arial, sans-serif;
  }
  .card {
    position: absolute;
    left: 171px;
    width: 825px;
    height: 471px;
    background: var(--card-white);
    border-radius: 26px;
    overflow: hidden;
    box-shadow: 0 4px 14px rgba(0,0,0,0.18);
  }
  .card--front { top: 106px; }
  .card--back { top: 639px; }

  .front-band { position: absolute; left: 0; top: 0; }
  .holder {
    position: absolute;
    left: 57px;
    top: 54px;
    color: var(--card-white);
  }
  .holder__name {
    font-family: "Exo 2", Arial, sans-serif;
    font-weight: 700;
    font-size: 31px;
    letter-spacing: 1px;
    line-height: 1.1;
  }
  .holder__role {
    font-family: "Roboto", Arial, sans-serif;
    font-weight: 500;
    font-size: 19px;
    margin-top: 2px;
  }
  .company-name {
    position: absolute;
    left: 40px;
    width: 400px;
    top: 288px;
    text-align: center;
    font-family: "Exo 2", Arial, sans-serif;
    font-weight: 700;
    font-size: 34px;
    line-height: 1.1;
    color: var(--brand-blue);
  }
  .divider {
    position: absolute;
    left: 430px;
    top: 247px;
    width: 1px;
    height: 140px;
    background: var(--rule-gray);
  }
  .contacts {
    position: absolute;
    left: 469px;
    top: 252px;
    list-style: none;
  }
  .contacts__item {
    display: flex;
    align-items: center;
    height: 43.5px;
    font-size: 19.5px;
    color: var(--text-gray);
  }
  .contacts__icon { width: 29px; height: 29px; margin-right: 21px; flex: none; }

  .back-name {
    position: absolute;
    left: 0;
    width: 100%;
    top: 200px;
    text-align: center;
    font-family: "Exo 2", Arial, sans-serif;
    font-weight: 700;
    font-size: 62px;
    color: var(--brand-blue);
  }
  .tagline {
    position: absolute;
    left: 0;
    width: 100%;
    top: 405px;
    text-align: center;
    font-family: "Exo 2", Arial, sans-serif;
    font-weight: 700;
    font-size: 20px;
    color: var(--brand-gray);
  }
  .tagline__accent { color: var(--brand-blue); }
</style>
</head>
<body>

<section class="card card--front">
  <svg class="front-band" width="825" height="180" viewBox="0 0 825 180" aria-hidden="true">
    <path d="M0 0 H535 C472 0 452 40 425 100 C398 158 378 178 318 178 H0 Z" fill="var(--brand-blue)"/>
  </svg>
  <div class="holder">
    <h1 class="holder__name">OWEN CASTELLANE</h1>
    <p class="holder__role">Owner/President - Auctioneer</p>
  </div>

  <p class="company-name">Marrowgate<br>Auctions</p>

  <div class="divider"></div>

  <ul class="contacts">
    <li class="contacts__item">
      <svg class="contacts__icon" viewBox="0 0 30 30" aria-hidden="true">
        <circle cx="15" cy="15" r="13" fill="none" stroke="var(--brand-blue)" stroke-width="2"/>
        <path d="M10.5 8.5 l2.5-.5 1.5 3.5-1.8 1.2 c.8 1.8 2 3 3.8 3.8 l1.2-1.8 3.5 1.5-.5 2.5 c-6 .5-11-4.5-10.2-10.2z" fill="var(--brand-blue)"/>
      </svg>
      702-555-0148
    </li>
    <li class="contacts__item">
      <svg class="contacts__icon" viewBox="0 0 30 30" aria-hidden="true">
        <circle cx="15" cy="15" r="13" fill="none" stroke="var(--brand-blue)" stroke-width="2"/>
        <rect x="8.5" y="10.5" width="13" height="9" rx="1" fill="var(--brand-blue)"/>
        <path d="M8.8 11 L15 15.5 L21.2 11" fill="none" stroke="#fff" stroke-width="1.2"/>
      </svg>
      hello@marrowgatebids.com
    </li>
    <li class="contacts__item">
      <svg class="contacts__icon" viewBox="0 0 30 30" aria-hidden="true">
        <circle cx="15" cy="15" r="13" fill="none" stroke="var(--brand-blue)" stroke-width="2"/>
        <circle cx="15" cy="15" r="7" fill="var(--brand-blue)"/>
        <path d="M8 15 H22 M15 8 C12 11 12 19 15 22 M15 8 C18 11 18 19 15 22" fill="none" stroke="#fff" stroke-width="1"/>
      </svg>
      bidharborgroup.com
    </li>
  </ul>
</section>

<section class="card card--back">
  <p class="back-name">Marrowgate Auctions</p>
  <p class="tagline"><span class="tagline__accent">Improving Charity</span> Auctions Nationwide</p>
</section>

</body>
</html>
```